Executive search firm in fashion, luxury and retail industry needs logo and card design.

We are a start-up recruiting firm that specializes in the retail and fashion industry, based in New York. We are looking for something that will appeal to CEO level clients and candidates, but that has a little design edge...not overly corporate but still CEO-appropriate. We have clean, sophisticated taste and want a contemporary feel. Happy to have a two sided card. Not afraid of a little color but it should be high-design, not gimmicky and tasteful.

Quillby Market(s)

CEO's, HR Leaders, in retail, fashion (i.e. Havenmere, Quillby, Otto Vasquel)

Industry/Entity Type

Professional Service

Contact Information for Business Card

Linden Row Talent Partners
Address to be determined
Alder Bay, ST 00147

Marla Tovick
Managing Director
(555)013-2846
mtovick@lindenrowtalent.example

Font styles to use
Serif
Sans Serif

Requirements
Must have
• clean lines, crisp graphics, some color. Prefer a graphic treatment over a "logo" per se. No pictures, etc.
Nice to have
• double sided design.
Should not have
• Gimmicks, smaltz, goop. Think Gallery of Current Forms, not the Pelham Vault. No earth tones, as in beige and brown, no pastels. Strong colors are fine in moderation. Grays are good. Jewel tones are good. No red.

```html
<!DOCTYPE html>
<html lang="en">
<head>
<meta charset="utf-8">
<title>Linden Row Talent Partners – Business Card</title>
<link rel="stylesheet" href="https://fonts.googleapis.com/css2?family=Tinos:wght@400;700&family=Arimo:wght@400&display=swap">
<style>
  :root {
    --stage: #e4e4e4;
    --paper: #ffffff;
    --ink: #111111;
    --royal: #3a4ba3;
    --black: #000000;
    --serif: "Tinos", "Times New Roman", serif;
    --sans: "Arimo", "Helvetica Neue", Arial, sans-serif;
  }
  html, body {
    margin: 0;
    padding: 0;
    width: 1200px;
    height: 933px;
    overflow: hidden;
    background: var(--stage);
  }
  .stage {
    position: relative;
    width: 1200px;
    height: 933px;
  }
  .card {
    position: absolute;
    left: 274px;
    width: 653px;
    height: 374px;
    overflow: hidden;
    box-shadow: 0 4px 14px rgba(0,0,0,0.25);
  }
  .card--front { top: 64px; background: var(--paper); }
  .card--back  { top: 494px; background: var(--black); }

  .swoosh {
    position: absolute;
    inset: 0;
    width: 100%;
    height: 100%;
  }
  .firm-name {
    position: absolute;
    margin: 0;
    font-family: var(--serif);
    font-weight: 700;
    line-height: 1;
    letter-spacing: -0.5px;
    white-space: nowrap;
  }
  .card--front .firm-name {
    left: 27px;
    top: 49px;
    font-size: 44px;
    color: var(--ink);
    transform: scaleX(0.95);
    transform-origin: left center;
  }
  .card--back .firm-name {
    left: 0;
    right: 0;
    top: 158px;
    text-align: center;
    color: var(--paper);
    font-size: 50px;
    transform: scaleX(0.94);
  }
  .person {
    position: absolute;
    left: 24px;
    top: 168px;
    font-family: var(--sans);
  }
  .person__name {
    margin: 0;
    font-size: 34px;
    line-height: 1;
    color: var(--royal);
  }
  .person__role {
    margin: 8px 0 0;
    font-size: 21px;
    line-height: 1.1;
    color: var(--ink);
  }
  .contact {
    position: absolute;
    right: 33px;
    top: 264px;
    margin: 0;
    padding: 0;
    list-style: none;
    font-family: var(--sans);
    font-size: 18px;
    color: var(--paper);
  }
  .contact__item {
    display: flex;
    justify-content: flex-end;
    align-items: center;
    height: 29.5px;
    gap: 12px;
    white-space: nowrap;
  }
  .contact__icon {
    width: 14px;
    height: 14px;
    flex: none;
  }
</style>
</head>
<body>
<main class="stage">

  <section class="card card--front" aria-label="Card front">
    <svg class="swoosh" viewBox="0 0 653 374" preserveAspectRatio="none" aria-hidden="true">
      <path d="M78,374 C360,320 560,180 549,0 L653,0 L653,374 Z" fill="var(--black)"/>
      <path d="M121,374 C411,299 601,149 621,0" fill="none" stroke="var(--paper)" stroke-width="2.5"/>
      <path d="M130,374 C420,300 610,150 630,0 L653,0 L653,374 Z" fill="var(--royal)"/>
    </svg>

    <h1 class="firm-name">Linden Row Talent Partners</h1>

    <div class="person">
      <p class="person__name">Marla Tovick</p>
      <p class="person__role">Managing Director</p>
    </div>

    <ul class="contact">
      <li class="contact__item">
        <span>(555)013-2846</span>
        <svg class="contact__icon" viewBox="0 0 14 14" aria-hidden="true">
          <rect width="14" height="14" rx="2" fill="var(--paper)"/>
          <path d="M3,6 Q7,2.5 11,6 L10,7 L8.5,6 L8.5,5 Q7,4.5 5.5,5 L5.5,6 L4,7 Z" fill="var(--royal)"/>
          <rect x="4" y="7.5" width="6" height="3.5" rx="0.8" fill="var(--royal)"/>
        </svg>
      </li>
      <li class="contact__item">
        <span>Alder Bay, ST 00147</span>
        <svg class="contact__icon" viewBox="0 0 14 14" aria-hidden="true">
          <rect width="14" height="14" rx="2" fill="var(--paper)"/>
          <path d="M7,12 C5,9 4,7.5 4,5.8 A3,3 0 0 1 10,5.8 C10,7.5 9,9 7,12 Z" fill="var(--royal)"/>
          <circle cx="7" cy="5.8" r="1.1" fill="var(--paper)"/>
        </svg>
      </li>
      <li class="contact__item">
        <span>mtovick@lindenrowtalent.example</span>
        <svg class="contact__icon" viewBox="0 0 14 14" aria-hidden="true">
          <rect width="14" height="14" rx="2" fill="var(--paper)"/>
          <rect x="2.5" y="4" width="9" height="6.5" fill="var(--royal)"/>
          <path d="M2.5,4 L7,8 L11.5,4" fill="none" stroke="var(--paper)" stroke-width="0.9"/>
        </svg>
      </li>
    </ul>
  </section>

  <section class="card card--back" aria-label="Card back">
    <h2 class="firm-name">Linden Row Talent Partners</h2>
  </section>

</main>
</body>
</html>
```